Dalton Power Supply, Inc. Business Card Design

We are an Electrical Distributor looking for a Modern, Professional Business Card design.

Target Market(s)

Residential Commercial Industrial

Industry/Entity Type

Electrical

Contact Information for Business Card

Dalton Power Supply, Inc.
418 Maple Ridge Lane
Brookvale, NC 27514
555-214-7630
555-214-8842 Fax
daltonpower@brightmail-example.net

```html
<!DOCTYPE html>
<html lang="en">
<head>
<meta charset="utf-8">
<title>Dalton Power Supply, Inc. – Business Card</title>
<link rel="stylesheet" href="https://fonts.googleapis.com/css2?family=Open+Sans:wght@600;700&display=swap">
<style>
  :root {
    --card-red: #f70d0d;
    --panel-light: #e9ecec;
    --panel-mid: #d3d8d9;
    --ink: #141414;
    --ink-soft: #222;
    --frame-dark: #3d4a52;
    --white: #ffffff;
    --icon-grey: #5b5f63;
  }
  * { margin: 0; padding: 0; box-sizing: border-box; }
  html, body { width: 1200px; height: 685px; overflow: hidden; background: var(--white); }
  .card {
    position: relative;
    width: 1200px; height: 685px;
    overflow: hidden;
    font-family: "Open Sans", Arial, sans-serif;
    background: var(--card-red);
  }
  .card__texture {
    position: absolute; left: 0; top: 0;
    width: 1200px; height: 340px;
    background: linear-gradient(120deg, var(--panel-mid) 0%, var(--panel-light) 40%, #f3f5f5 60%, var(--panel-mid) 100%);
  }
  .card__lines { position: absolute; left: 0; top: 0; }
  .brand {
    position: absolute; left: 84px; top: 66px;
    display: flex; align-items: center; gap: 34px;
  }
  .brand__name {
    font-size: 55px; font-weight: 700; color: var(--ink);
    letter-spacing: -0.5px; white-space: nowrap; line-height: 1;
  }
  .brand__mark {
    width: 78px; height: 78px; background: var(--card-red);
  }
  .person { position: absolute; left: 129px; top: 222px; color: var(--ink-soft); }
  .person__name { font-size: 40px; font-weight: 600; line-height: 1.1; }
  .person__role { font-size: 29px; font-weight: 600; margin-top: 8px; }
  .contact {
    position: absolute; color: var(--white); font-weight: 600;
    font-size: 32px; line-height: 1.45; white-space: nowrap;
  }
  .contact--address { left: 136px; top: 388px; }
  .contact--email { left: 136px; top: 496px; font-size: 29px; }
  .contact--web { left: 136px; top: 568px; }
  .contact--phone { left: 818px; top: 420px; }
  .contact--fax { left: 818px; top: 512px; }
</style>
</head>
<body>
<div class="card">
  <div class="card__texture" role="img" aria-label="Soft grey low-poly geometric background"></div>

  <svg class="card__lines" width="1200" height="685" viewBox="0 0 1200 685">
    <defs>
      <clipPath id="upper-zone"><rect x="0" y="0" width="1200" height="340"/></clipPath>
      <clipPath id="lower-zone"><rect x="0" y="340" width="1200" height="345"/></clipPath>
    </defs>
    <path d="M773 200 H1089 Q1109 200 1109 180 V0" fill="none" stroke="var(--frame-dark)" stroke-width="4"/>
    <path class="frame" clip-path="url(#upper-zone)" d="M773 200 H107 Q87 200 87 220 V609 Q87 629 107 629 H753 Q773 629 773 609 Z" fill="none" stroke="var(--card-red)" stroke-width="4"/>
    <path class="frame" clip-path="url(#lower-zone)" d="M773 200 H107 Q87 200 87 220 V609 Q87 629 107 629 H753 Q773 629 773 609 Z" fill="none" stroke="var(--white)" stroke-width="4"/>
    <polygon points="773,191 781,196 781,204 773,209 765,204 765,196" fill="var(--card-red)"/>

    <g fill="var(--white)">
      <circle cx="87" cy="420" r="27"/>
      <circle cx="87" cy="513" r="27"/>
      <circle cx="87" cy="596" r="27"/>
      <circle cx="773" cy="436" r="27"/>
      <circle cx="773" cy="533" r="27"/>
    </g>

    <g fill="none" stroke="var(--icon-grey)" stroke-width="2.2" stroke-linecap="round" stroke-linejoin="round">
      <!-- pin -->
      <path d="M87 434 C80 425 76 420 76 414 A11 11 0 0 1 98 414 C98 420 94 425 87 434 Z"/>
      <circle cx="87" cy="414" r="4"/>
      <!-- envelope -->
      <rect x="74" y="504" width="26" height="18" rx="1.5"/>
      <path d="M74 505 L87 515 L100 505"/>
      <!-- link -->
      <path d="M84 599 L80 603 A5 5 0 0 1 73 596 L79 590 A5 5 0 0 1 86 590"/>
      <path d="M90 593 L94 589 A5 5 0 0 1 101 596 L95 602 A5 5 0 0 1 88 602"/>
      <path d="M83 600 L91 592"/>
      <!-- phones -->
      <path d="M764 424 L769 424 L771 431 L768 434 C770 439 772 441 777 443 L780 440 L787 442 L787 447 C787 449 785 450 783 450 C771 449 762 440 761 428 C761 426 762 424 764 424 Z"/>
      <path d="M764 521 L769 521 L771 528 L768 531 C770 536 772 538 777 540 L780 537 L787 539 L787 544 C787 546 785 547 783 547 C771 546 762 537 761 525 C761 523 762 521 764 521 Z"/>
    </g>
  </svg>

  <div class="brand">
    <span class="brand__name">Dalton Power Supply, Inc.</span>
    <span class="brand__mark"></span>
  </div>

  <div class="person">
    <p class="person__name">EVAN MERCER</p>
    <p class="person__role">Sales Manager</p>
  </div>

  <p class="contact contact--address">418 Maple Ridge Lane<br>Brookvale, NC 27514</p>
  <p class="contact contact--email">daltonpower@brightmail-example.net</p>
  <p class="contact contact--web">www.daltonpower-example.com</p>
  <p class="contact contact--phone">Phone: 555-214-7630</p>
  <p class="contact contact--fax">Fax : 555-214-8842</p>
</div>
</body>
</html>
```